Manufacturing company needs new business card.

I need a unique Business Card that will truly stand out. Nothing too busy. Simple is good, right? Not looking for a standard design either. No cookie cutter layout. I am just looking for something interesting and a bit different. Does't have to completely off the wall crazy, just not your run of the mill business card. Clean and modern with a touch of industrial.

Target Market(s)

Air conditioning industry, Architects, builders.

Industry/Entity Type

Business

Contact Information for Business Card

Details to be included on card are:

Peter Vance
Managing Director

T: 1300 847 519
M: 0428 593 174
W: www.brenvaleworks.com.au
E: peter.vance@brenvaleworks.com.au
A: 58 Harwick Lane, Sydney NSW 2000

Font styles to use
Sans Serif

Colors
0355a3
848484
fbfbfb

Requirements
Must have
• Card design must be landscape.

```html
<!DOCTYPE html>
<html lang="en">
<head>
<meta charset="utf-8">
<title>Brenvale Works – Business Card</title>
<link rel="stylesheet" href="https://fonts.googleapis.com/css2?family=Open+Sans:wght@400;600;700&display=swap">
<style>
  :root {
    --brand-blue: #0355a3;
    --brand-grey: #848484;
    --brand-white: #fbfbfb;
    --page-bg: #e9e9e9;
    --metal-light: #d4d4d4;
    --metal-mid: #b4b4b4;
    --metal-dark: #8f8f8f;
    --panel-tint: rgba(255, 255, 255, 0.18);
  }
  html, body {
    margin: 0;
    padding: 0;
    width: 1200px;
    height: 853px;
    overflow: hidden;
    background: var(--page-bg);
    font-family: "Open Sans", Arial, sans-serif;
  }
  .canvas {
    position: relative;
    width: 1200px;
    height: 853px;
    display: flex;
    align-items: center;
    justify-content: center;
    gap: 40px;
  }
  .card {
    position: relative;
    width: 540px;
    height: 330px;
    border-radius: 22px;
    overflow: hidden;
    background: linear-gradient(160deg, var(--metal-light) 0%, var(--metal-mid) 55%, var(--metal-dark) 100%);
    box-shadow: 0 10px 28px rgba(0, 0, 0, 0.25);
  }
  .brand {
    position: absolute;
    top: 34px;
    left: 36px;
    display: flex;
    align-items: center;
    gap: 16px;
  }
  .brand-square {
    width: 46px;
    height: 46px;
    background: var(--brand-blue);
    border-radius: 4px;
  }
  .brand-name {
    font-size: 40px;
    font-weight: 600;
    color: var(--brand-blue);
    letter-spacing: -0.5px;
    line-height: 1;
  }
  .side-panel {
    position: absolute;
    top: 120px;
    right: 0;
    width: 220px;
    height: 210px;
    background: var(--panel-tint);
    border-top-left-radius: 22px;
  }
  .holder {
    position: absolute;
    left: 40px;
    top: 172px;
  }
  .holder-name {
    margin: 0;
    font-size: 38px;
    font-weight: 700;
    color: var(--brand-white);
    line-height: 1.1;
    text-shadow: 0 1px 2px rgba(0, 0, 0, 0.25);
  }
  .holder-role {
    margin: 6px 0 0 2px;
    font-size: 19px;
    font-weight: 600;
    color: var(--brand-blue);
  }
  .contact-list {
    position: absolute;
    left: 52px;
    top: 128px;
    margin: 0;
    padding: 0;
    list-style: none;
    font-size: 18px;
    line-height: 34px;
    color: var(--brand-white);
  }
  .contact-list li {
    display: flex;
  }
  .contact-label {
    width: 34px;
    color: var(--brand-blue);
    font-weight: 600;
  }
</style>
</head>
<body>
  <main class="canvas">
    <section class="card card-back" aria-label="Card back with contact details">
      <div class="brand">
        <div class="brand-square"></div>
        <span class="brand-name">Brenvale Works</span>
      </div>
      <ul class="contact-list">
        <li><span class="contact-label">t:</span>1300 847 519</li>
        <li><span class="contact-label">m:</span>0428 593 174</li>
        <li><span class="contact-label">e:</span>peter.vance@brenvaleworks.com.au</li>
        <li><span class="contact-label">a:</span>58 Harwick Lane, Sydney NSW 2000</li>
        <li><span class="contact-label">w:</span>brenvaleworks.com.au</li>
      </ul>
    </section>

    <section class="card card-front" aria-label="Card front with name and title">
      <div class="brand">
        <div class="brand-square"></div>
        <span class="brand-name">Brenvale Works</span>
      </div>
      <div class="side-panel"></div>
      <div class="holder">
        <h1 class="holder-name">Peter Vance</h1>
        <p class="holder-role">Managing Director</p>
      </div>
    </section>
  </main>
</body>
</html>
```